School annual plan - describing all our goals for 2026

This is a high school plan. The design should be similar in style to other school flyers and posters.

2026 Kestwick SHS AIP - the document to design. Please make 1 page.

Documents to follow style:
Document 1: the 2025 School Annual Plan (use this for formatting. Change style to similar to Documents 2 & 3).

Document 2: the Kestwick Instructional Model - make the style similar to this.

Document 3: Explicit Instruction Classroom Matrix - Another document to make the style similar to.

This is the school's website: https://kestwickshs.lornavale.edu.au/

Please let me know if you have any questions.

```html
<!DOCTYPE html>
<html lang="en">
<head>
<meta charset="utf-8">
<title>Kestwick State High School – 2026 Annual Implementation Plan</title>
<link href="https://fonts.googleapis.com/css2?family=Montserrat:wght@500;600;700;800&display=swap" rel="stylesheet">
<style>
:root{
  --navy:#003a70;
  --yellow:#f0e35a;
  --pale:#f5f0a8;
  --blue:#bfcfe8;
  --ink:#0c1a2e;
  --page:#ffffff;
}
*{box-sizing:border-box;margin:0;padding:0}
html,body{width:1200px;height:1200px;overflow:hidden;background:var(--page)}
body{font-family:"Montserrat",Arial,sans-serif;color:var(--ink);position:relative}
.plan{position:absolute;left:20px;top:189px;width:1160px;height:822px;background:#fff}
.box{position:absolute}
.navy{background:var(--navy);color:#fff}
.yellow{background:var(--yellow)}
.pale{background:var(--pale)}
.blue{background:var(--blue)}
.round-tl{border-top-left-radius:6px}

/* header */
.masthead{left:0;top:24px;width:1160px;height:103px}
.school-mark{position:absolute;left:110px;top:30px;display:flex;align-items:center;gap:8px}
.school-mark .dot{width:34px;height:34px;border-radius:50%;background:var(--yellow)}
.school-mark .name{font-size:13px;font-weight:700;color:#fff}
.title{position:absolute;left:320px;top:8px;width:738px;text-align:center;font-size:38px;font-weight:800;letter-spacing:2.6px;color:#fff;line-height:46px}
.title-rule{position:absolute;left:327px;top:53px;width:724px;height:2px;background:var(--yellow)}
.subtitle{position:absolute;left:327px;top:58px;width:724px;text-align:center;font-size:24px;font-weight:700;letter-spacing:1.6px;color:var(--yellow)}

/* labels */
.label{font-size:10.5px;font-weight:700;line-height:1.05;padding:11px 10px}
.label.sm{padding:11px 4px 0 5px}
.priority-text{font-size:9.5px;font-weight:600;color:var(--ink);line-height:1.1}
.priority-text .kicker{color:var(--navy);font-weight:700;display:block;margin-bottom:7px}

.monitor-head{height:23px;text-align:center;font-size:10.5px;font-weight:600;line-height:23px;border-radius:6px 6px 0 0}
.terms{display:flex;height:30px}
.terms span{flex:1;background:var(--pale);border-left:1px solid #fff;font-size:4.8px;font-weight:700;color:var(--navy);text-align:center;padding-top:3px}
.terms span:first-child{border-left:0}

.focus h3{font-size:9.3px;font-weight:600;margin-bottom:2px}
ul.dots{list-style:none}
ul.dots li{font-size:6.4px;font-weight:600;line-height:9px;padding-left:7px;text-indent:-5px}
ul.dots li::before{content:"•";margin-right:2px}

.section-bar{height:22px;font-size:10.5px;font-weight:700;line-height:22px;padding-left:10px}
.section-bar small{font-size:6.8px;font-weight:700}
.section-bar .hl{color:var(--yellow)}

/* success criteria */
.vlabel{display:flex;align-items:center;justify-content:center}
.vlabel span{transform:rotate(-90deg);white-space:nowrap;font-size:10px;font-weight:700}
.vlabel.on-yellow span{color:var(--navy)}
.block-title{position:absolute;font-size:12.5px;font-weight:700;color:var(--navy)}
.col{position:absolute}
.col h4{font-size:8.5px;font-weight:700;line-height:1.25;margin-bottom:6px}

/* red tape */
.tape-head{left:30px;top:734px;width:1102px;height:24px;text-align:center;font-size:10.5px;font-weight:600;line-height:24px}
.tape{left:30px;top:758px;width:1102px;height:37px;border-radius:0 0 8px 8px}
.tape-item{position:absolute;top:0;height:37px;display:flex;align-items:center;gap:10px;font-size:6.8px;font-weight:600;line-height:9.5px}
.num{width:15px;height:15px;border-radius:50%;background:var(--navy);color:#fff;font-size:8.5px;font-weight:700;display:flex;align-items:center;justify-content:center;flex:none}
</style>
</head>
<body>
<main class="plan">

  <header class="box navy masthead">
    <div class="school-mark"><span class="dot"></span><span class="name">Kestwick SHS</span></div>
    <h1 class="title">KESTWICK STATE HIGH SCHOOL</h1>
    <div class="title-rule"></div>
    <p class="subtitle">2026 Annual Implementation Plan</p>
  </header>

  <!-- Priority 1 -->
  <div class="box navy label round-tl" style="left:30px;top:146px;width:85px;height:53px">School priority 1</div>
  <div class="box yellow priority-text" style="left:117px;top:146px;width:324px;height:53px;padding:6px 10px 0 24px">
    <span class="kicker">Belonging and Engagement</span>
    In classrooms: Pedagogy-whole school focus on pedagogy and “How Kestwick Students Learn”
  </div>
  <div class="box" style="left:443px;top:146px;width:173px;height:53px">
    <div class="monitor-head navy">Monitoring</div>
    <div class="terms"><span>Term 1</span><span>Term 2</span><span>Term 3</span><span>Term 4</span></div>
  </div>

  <!-- Priority 2 -->
  <div class="box navy label round-tl" style="left:618px;top:146px;width:78px;height:53px">School priority 2</div>
  <div class="box yellow priority-text" style="left:698px;top:146px;width:302px;height:53px;padding:15px 10px 0 31px">
    <span class="kicker" style="margin-bottom:5px">Curriculum-</span>
    Continued improvement Year 7-12 curriculum
  </div>
  <div class="box" style="left:1002px;top:146px;width:130px;height:53px">
    <div class="monitor-head navy">Monitoring</div>
    <div class="terms"><span>Term 1</span><span>Term 2</span><span>Term 3</span><span>Term 4</span></div>
  </div>

  <!-- Link rows -->
  <div class="box navy label" style="left:30px;top:201px;width:85px;height:74px">Link to school improvement strategy:</div>
  <div class="box blue focus" style="left:117px;top:201px;width:499px;height:74px;padding:4px 10px 0 11px">
    <h3>Our 2026 focus area for improvement is to:</h3>
    <ul class="dots" style="padding-left:25px">
      <li>Enact planned and intentional pedagogical practices that align to How Kestwick Students Learn</li>
      <li>Conduct regular in-class observation and feedback cycles</li>
      <li>Deliver intensive pedagogy support for teachers using classroom profiling, walkthroughs and structured feedback in explicit instruction pedagogy</li>
      <li>Adopt clear processes to track, monitor and differentiate support so that every child is learning and improving</li>
      <li>Drive Digital Innovation through the integration of LearnSpace.</li>
    </ul>
  </div>
  <div class="box navy label sm" style="left:618px;top:201px;width:78px;height:74px">Link to school improvement strategy:</div>
  <div class="box blue focus" style="left:698px;top:201px;width:434px;height:74px;padding:4px 8px 0 11px">
    <h3>Our 2026 focus area for improvement is to:</h3>
    <ul class="dots">
      <li>Deliver an aligned and engaging curriculum that is regularly reviewed as part of a quality assurance cycle</li>
      <li>Enact a Whole-School Moderation Policy ensuring alignment, validity, and reliability of teacher judgments: before, after, end</li>
      <li>Deepen the school’s Reading Strategy under MTSS, targeting Tier 1, 2, and 3 interventions</li>
      <li>Complete full alignment to Core Curriculum R9, ensuring consistency across Years 7–10</li>
      <li>Strengthen LCE attainment and pathways monitoring for Years 10–12 students.</li>
    </ul>
  </div>

  <!-- Strategies -->
  <div class="box navy label" style="left:30px;top:277px;width:85px;height:57px">Strategies</div>
  <div class="box blue" style="left:117px;top:277px;width:499px;height:57px;padding:7px 10px 0 36px">
    <ul class="dots">
      <li>Line Management, quality assurance, setting professional goals (SPG)</li>
      <li>Observation and Feedback Framework</li>
      <li>Classroom Profiling</li>
      <li>Differentiated approaches to pedagogy</li>
      <li>Digital Pedagogy</li>
    </ul>
  </div>
  <div class="box navy label sm" style="left:618px;top:277px;width:78px;height:57px">Strategy/ies</div>
  <div class="box blue" style="left:698px;top:277px;width:434px;height:57px;padding:7px 8px 0 12px;display:flex;gap:30px">
    <ul class="dots" style="width:165px">
      <li>Teaching and Learning- all HoD aligned</li>
      <li>Line Management- quality assurance</li>
      <li>Whole school walk-throughs</li>
      <li>Moderation- before, after, end</li>
      <li>Whole School Reading Strategy</li>
    </ul>
    <ul class="dots">
      <li>R9 Core Curriculum with accessible assessment</li>
      <li>Maximising Learning Team and collaboration time</li>
      <li>Widen VET options in Senior School</li>
      <li>Senior School Pathways document.</li>
    </ul>
  </div>

  <!-- Actions & resources -->
  <div class="box navy section-bar" style="left:30px;top:336px;width:411px"><span class="hl">Actions:</span> <small>including Responsible role(s)</small></div>
  <div class="box navy section-bar" style="left:443px;top:336px;width:173px;padding-left:7px">Resources</div>
  <div class="box navy section-bar" style="left:618px;top:336px;width:382px"><span class="hl">Actions:</span> <small>including Responsible role(s)</small></div>
  <div class="box navy section-bar" style="left:1002px;top:336px;width:130px;text-align:center;padding-left:0">Resources</div>

  <div class="box pale" style="left:30px;top:360px;width:411px;height:73px;padding:4px 8px 0 8px">
    <ul class="dots">
      <li>Visible, planned and intentional pedagogical practices in all learning environments</li>
      <li>Quality assurance, line of sight, professional learning, meetings, classrooms, feedback</li>
      <li>Continue to embed LearnSpace as the core platform for curriculum programs, and resources</li>
      <li>Enact professional development for pedagogical practices, classroom profiling and digital learning for all staff</li>
      <li>100% of teachers engaged in at least one Observation and Feedback cycle per semester</li>
      <li>Continue “How Kestwick Students Learn”</li>
      <li>Every teacher being observed through walkthroughs from leadership.</li>
    </ul>
  </div>
  <div class="box yellow" style="left:443px;top:360px;width:173px;height:73px;padding:10px 6px 0 7px">
    <ul class="dots">
      <li>Kestwick HITS</li>
      <li>Critical Routines</li>
      <li>CSCMs</li>
      <li>How Kestwick Students Learn</li>
      <li>Classroom Observation and Feedback Cycle</li>
      <li>MTSS documents</li>
    </ul>
  </div>
  <div class="box pale" style="left:618px;top:360px;width:382px;height:73px;padding:10px 8px 0 10px">
    <ul class="dots">
      <li>Continue to embed LearnSpace as the core platform for curriculum programs, and resources in Year 7 &amp; 8 Core, VET and Year 11 &amp; 12 for assessment submission “</li>
      <li>Continue implementation of Core Curriculum R9</li>
      <li>Continue to deliver 2024 LCAA Applied syllabuses and 2025 LCAA General syllabuses</li>
      <li>Increase VET options to meet the needs of our learners, priority in Year 10 2026</li>
      <li>Enact differentiated curriculum that meets the individual needs of students in classrooms</li>
    </ul>
  </div>
  <div class="box yellow" style="left:1002px;top:360px;width:130px;height:73px;padding:4px 4px 0 9px">
    <ul class="dots">
      <li>LearnSpace</li>
      <li>ClassChat</li>
      <li>Data Plan</li>
      <li>StudyForward NCRA</li>
      <li>LCAA</li>
      <li>LCRF- K-12 Framework</li>
      <li>DoL Curriculu</li>
    </ul>
  </div>

  <!-- End of year success criteria -->
  <div class="box navy vlabel" style="left:30px;top:433px;width:29px;height:298px"><span>End of Year Success Criteria</span></div>
  <div class="box navy vlabel" style="left:61px;top:433px;width:52px;height:233px"><span>Measures</span></div>
  <div class="box yellow vlabel on-yellow" style="left:61px;top:668px;width:52px;height:63px"><span>Artefacts</span></div>

  <section class="box blue" style="left:115px;top:433px;width:1017px;height:131px">
    <h2 class="block-title" style="left:21px;top:8px">Performance:</h2>
    <div class="col" style="left:21px;top:31px;width:190px">
      <h4>AIP measurable/desired outcomes engagement:</h4>
      <ul class="dots">
        <li>10% Reduction in behaviour incidents</li>
        <li>8% SDA rate- whole school</li>
        <li>90% Attendance</li>
        <li>Improved student retention</li>
        <li>VET- 100% CERT II</li>
        <li>Out of Catchment enrolments &lt;20% (24% in 2025)</li>
      </ul>
    </div>
    <div class="col" style="left:226px;top:31px;width:200px">
      <h4>AIP measurable/desired outcomes engagement:</h4>
      <ul class="dots">
        <li>10% Reduction in behaviour incidents</li>
        <li>8% SDA rate- whole school</li>
        <li>90% Attendance</li>
        <li>Improved student retention</li>
        <li>VET- 100% CERT II</li>
        <li>Out of Catchment enrolments &lt;20% (24% in 2025)</li>
      </ul>
    </div>
    <div class="col" style="left:440px;top:26px;width:390px">
      <h4>Long term measurable/desired outcomes:</h4>
      <ul class="dots">
        <li>Increase in proportion of students achieving a C and above in all subjects with a focus on English and Maths</li>
        <li>Increase in proportion of students achieving an A or B in all subjects with a focus on English and Maths</li>
        <li>Maintain 100% of students achieving a LCE/ LCIA</li>
        <li>Improved rates of student attendance- days of learning</li>
        <li>Reduction in school disciplinary absence rates</li>
        <li>Improved Year 13 Pathways Survey Results</li>
        <li>Improved First Nations Outcomes- Narrowing the Gap- attendance and academic outcomes</li>
        <li>Improved participation and performance in NAPTA</li>
      </ul>
    </div>
    <div class="col" style="left:835px;top:33px;width:175px">
      <h4>AIP measurable/desired outcomes performance (whole school):</h4>
      <ul class="dots">
        <li>45% A-B</li>
        <li>90% A-C</li>
        <li>100% A-D</li>
        <li>100% LCE/LCIA (Year 12 2026)</li>
      </ul>
    </div>
  </section>

  <section class="box pale" style="left:115px;top:567px;width:1017px;height:99px">
    <h2 class="block-title" style="left:16px;top:5px">Behaviour</h2>
    <div class="col" style="left:16px;top:28px;width:400px">
      <h4>Staff will:</h4>
      <ul class="dots">
        <li>Apply the Critical Routines, Core Skills for Classroom Management and How Kestwick Students Learn</li>
        <li>Access agreed data sets to know their learners, plan and differentiate to ensure accessibility for all students</li>
        <li>Use Muti Tiered Systems of Support and the Student Referral Team to support behaviour, academics, and wellbeing to improve outcomes for students</li>
        <li>Utilise LearnSpace for all 7, 8, Senior School Submissions and VET classes from 2026</li>
      </ul>
    </div>
    <div class="col" style="left:428px;top:28px;width:110px">
      <h4>Students will:</h4>
      <ul class="dots">
        <li>Be prepared and ready for learning and follow Critical Routines</li>
        <li>Know, what, how and why they are learning</li>
      </ul>
    </div>
    <div class="col" style="left:577px;top:28px;width:225px">
      <h4>Education Support Officers will:</h4>
      <ul class="dots">
        <li>Maximise their time in classrooms with students- face to face</li>
        <li>Support the students in classrooms, in year level hubs, in the reset room and in alternative learning environments.</li>
      </ul>
    </div>
    <div class="col" style="left:836px;top:28px;width:175px">
      <h4>Leadership Team will:</h4>
      <ul class="dots">
        <li>Support all teaching and non- teaching staff</li>
        <li>Demostrate Instructional Leadership</li>
        <li>Display visible leadership in the classroom/s.</li>
      </ul>
    </div>
  </section>

  <div class="box blue" style="left:115px;top:668px;width:506px;height:63px;padding:12px 0 0 16px">
    <ul class="dots">
      <li>Moderation Plan- Before, After, End, including a HOD planned collaboration cycle</li>
      <li>Staff Collaborative Planning Outcomes</li>
      <li>Three Levels of Planning</li>
      <li>Curriculum Aligned Marking Guides</li>
    </ul>
  </div>
  <div class="box blue" style="left:624px;top:668px;width:508px;height:63px;padding:12px 0 0 186px">
    <ul class="dots">
      <li>LearnSpace - Resourcing and Unit Plans</li>
      <li>ALRAs</li>
      <li>Assessment Calendar</li>
      <li>Maximising Learning Team Outcomes</li>
    </ul>
  </div>

  <!-- Red tape -->
  <div class="box navy tape-head">Reduction of red tape in day-to-day work, planning and processes include:</div>
  <div class="box yellow tape">
    <div class="tape-item" style="left:37px"><span class="num">1</span><span style="margin-left:4px">Kestwick Strategy -<br>Ask: Is this the best way to do it? How do we keep it simple?</span></div>
    <div class="tape-item" style="left:322px"><span class="num">2</span><span>Strategic Meeting Scheduling</span></div>
    <div class="tape-item" style="left:493px"><span class="num">3</span><span>Investigate assessment submission</span></div>
    <div class="tape-item" style="left:677px"><span class="num">4</span><span>NDSA data collection to be reviewed</span></div>
    <div class="tape-item" style="left:878px"><span class="num">5</span><span style="margin-left:14px">Increase use of StudyForward<br>for student work at home requirements</span></div>
  </div>

</main>
</body>
</html>
```